Webdesign Bestattungswesen Wiesentrup
Zielgruppe
Bestattungsunternehmen
Aufgabenstellung
- Seite soll keine Kopie der alten Webseite werden
- Logo muss unverändert bleiben
- KEIN schwarz als Hauptfarbe !
- sanfte Farben

```html
<!DOCTYPE html>
<html lang="de">
<head>
<meta charset="utf-8">
<title>Bestattungswesen Wiesentrup – Würdevolle Bestattungen</title>
<link href="https://fonts.googleapis.com/css2?family=Playfair+Display:wght@500;600&family=Poppins:wght@400;500;600&display=swap" rel="stylesheet">
<style>
:root{
  --bg:#f2f0eb;
  --ink:#4a3a1c;
  --text:#6b6458;
  --gold:#d3a23a;
  --gold-soft:#ecd9aa;
  --line:#d9cfb6;
  --card:#ffffff;
  --placeholder:#d6d2cc;
  --footer:#6f6861;
  --footer-bar:#5f5851;
  --footer-text:#f1ede6;
}
*{box-sizing:border-box;margin:0;padding:0}
html,body{width:1200px;height:3058px;overflow:hidden}
body{background:var(--bg);font-family:"Poppins",sans-serif;color:var(--text);position:relative}
.abs{position:absolute}

/* header */
.nav-pill{position:absolute;top:36px;height:30px;padding:0 11px;background:#fff;border-radius:15px;font-size:11px;font-weight:500;color:var(--ink);display:flex;align-items:center;gap:6px}
.brand{position:absolute;left:0;width:1200px;top:14px;text-align:center}
.brand-dot{width:26px;height:26px;border-radius:50%;background:var(--gold);margin:0 auto 42px}
.brand-name{font-family:"Playfair Display",serif;font-size:23px;font-weight:500;color:var(--ink)}
.reach{position:absolute;top:18px;left:967px;font-size:11px;color:var(--text)}
.phone-btn{position:absolute;display:flex;align-items:center;justify-content:center;gap:8px;background:var(--gold);color:var(--ink);border-radius:16px;font-weight:600}
.phone-btn svg{width:18px;height:18px}

/* hero */
.hero{position:absolute;left:88px;top:146px;width:1024px;height:412px;border-radius:26px;overflow:hidden;
  background:radial-gradient(ellipse at 20% 20%,#fbfaf6 0%,#eef0ec 35%,transparent 60%),linear-gradient(115deg,#f6f4ef 0%,#e5e8e6 40%,#cfe0ea 75%,#b9d4e6 100%)}
.hero h1{position:absolute;left:0;right:0;top:116px;text-align:center;font-family:"Playfair Display",serif;font-weight:500;font-size:44px;line-height:57px;color:var(--ink)}
.hero p{position:absolute;left:0;right:0;top:252px;text-align:center;font-family:"Playfair Display",serif;font-size:21px;font-weight:500;color:#2f2a20}

/* intro */
.intro-title{left:88px;top:626px;width:500px;font-family:"Playfair Display",serif;font-size:22px;line-height:30px;font-weight:500;color:var(--ink)}
.intro-text{left:88px;top:700px;width:505px;font-size:12.5px;line-height:19px}
.intro-text p+p{margin-top:19px}
.intro-note{left:88px;top:942px;font-family:"Playfair Display",serif;font-size:16px;font-weight:600;color:var(--ink)}

.photo{position:absolute;overflow:hidden;border-radius:24px}
.tab{position:absolute;right:0;bottom:0;background:var(--bg);border-top-left-radius:24px;display:flex;align-items:center;gap:18px;font-family:"Playfair Display",serif;font-weight:600;color:var(--ink)}
.arrow{width:26px;height:26px;border-radius:50%;background:var(--gold-soft);display:flex;align-items:center;justify-content:center;flex:none}
.arrow svg{width:14px;height:14px}

.section-title{font-family:"Playfair Display",serif;font-size:23px;font-weight:500;color:var(--ink)}

/* service */
.card{position:absolute;width:329px;height:328px;border-radius:24px;overflow:hidden}
.card .fill{position:absolute;inset:0}
.card .tab{height:72px;padding:0 18px 0 20px;font-size:16.5px}
.text-card{background:var(--card);padding:32px 33px}
.text-card h3{font-family:"Playfair Display",serif;font-weight:500;font-size:22px;color:var(--ink);margin-top:14px;margin-bottom:10px}
.text-card p{font-size:12.5px;line-height:19px;width:250px}
.text-card .arrow{position:absolute;right:27px;bottom:24px}

/* faq */
.faq{position:absolute;left:264px;top:1898px;width:674px}
.faq-item{height:47.5px;border-bottom:1px solid var(--line);display:flex;align-items:center;gap:30px;padding-left:4px;font-family:"Playfair Display",serif;font-weight:600;font-size:16px;color:var(--ink)}
.faq-item svg{width:16px;height:16px}

/* memberships */
.member{position:absolute;top:2293px;width:241px;height:240px;background:var(--card);border-radius:22px;display:flex;align-items:center;justify-content:center}
.badge{background:var(--placeholder);width:140px;height:160px;border-radius:4px}

/* footer */
.footer{position:absolute;left:0;top:2594px;width:1200px;height:378px;background:var(--footer);color:var(--footer-text)}
.footer-bar{position:absolute;left:0;top:2972px;width:1200px;height:86px;background:var(--footer-bar);color:var(--footer-text);font-size:12.5px}
.f-brand{position:absolute;left:89px;top:48px;display:flex;align-items:center;gap:12px;font-family:"Playfair Display",serif;font-size:21px;font-weight:500}
.f-brand span.dot{width:22px;height:22px;border-radius:50%;background:var(--footer-text)}
.f-addr{position:absolute;left:89px;top:152px;font-size:12.5px;line-height:19px}
.f-addr strong{font-weight:600}
.f-contact{position:absolute;left:89px;display:flex;align-items:center;gap:14px;font-size:12.5px}
.f-contact svg{width:19px;height:19px}
.f-col{position:absolute;top:152px}
.f-col h4{font-family:"Playfair Display",serif;font-weight:600;font-size:16px;margin-bottom:10px}
.f-col li{list-style:none;font-size:12.5px;line-height:25px}
.map{position:absolute;left:783px;top:155px;width:329px;height:166px;border-radius:14px;background:linear-gradient(135deg,#eef0f0 0%,#e2e8e8 50%,#d9e9ee 100%)}
</style>
</head>
<body>

<header>
  <div class="nav-pill" style="left:88px">Bestattungsformen
    <svg width="9" height="9" viewBox="0 0 10 10" fill="none" stroke="currentColor" stroke-width="1.4"><path d="M2 3.5l3 3 3-3"/></svg>
  </div>
  <div class="nav-pill" style="left:235px">Vorsorge</div>
  <div class="nav-pill" style="left:316px">Bestattungskosten</div>
  <div class="brand">
    <div class="brand-dot"></div>
    <div class="brand-name">Bestattungswesen Wiesentrup</div>
  </div>
  <div class="nav-pill" style="left:781px">Über uns</div>
  <div class="nav-pill" style="left:862px">Kontakt</div>
  <div class="reach">rund um die Uhr erreichbar</div>
  <a class="phone-btn" style="left:967px;top:36px;width:145px;height:31px;font-size:13px">
    <svg viewBox="0 0 24 24" fill="none" stroke="currentColor" stroke-width="1.6"><path d="M5 3h4l2 5-2.5 1.5a11 11 0 005 5L15 12l5 2v4a2 2 0 01-2 2A16 16 0 013 5a2 2 0 012-2z"/></svg>
    03721 / 48 210
  </a>
</header>

<section class="hero" role="img" aria-label="Zarte weiße Kirschblüten vor hellblauem, unscharfem Hintergrund">
  <h1>Bestattungswesen Wiesentrup –<br>Würdevolle Bestattungen</h1>
  <p>Erinnerungen, Gedanken, letzte Worte ...</p>
</section>

<section>
  <h2 class="abs intro-title">Bestattungswesen Wiesentrup – Bestattung und Vorsorge in besten Händen.</h2>
  <div class="abs intro-text">
    <p>Eines Tages aber beschloß eine kleine Zeile Blindtext, ihr Name war Lorem Ipsum, hinaus zu gehen in die weite Grammatik. Der große Oxmox riet ihr davon ab, da es dort wimmele von bösen Kommata, wilden Fragezeichen und hinterhältigen Semikoli, doch das Blindtextchen ließ sich nicht beirren.</p>
    <p>Als es die ersten Hügel des Kursivgebirges erklommen hatte, warf es einen letzten Blick zurück auf die Skyline seiner Heimatstadt Buchstabhausen, die Headline von Alphabetdorf &nbsp;und die Subline seiner eigenen Straße, der Zeilengasse.</p>
  </div>
  <a class="phone-btn" style="left:88px;top:895px;width:144px;height:30px;font-size:12.5px">
    <svg viewBox="0 0 24 24" fill="none" stroke="currentColor" stroke-width="1.6"><path d="M5 3h4l2 5-2.5 1.5a11 11 0 005 5L15 12l5 2v4a2 2 0 01-2 2A16 16 0 013 5a2 2 0 012-2z"/></svg>
    03721 / 48 210
  </a>
  <p class="abs intro-note">Wir sind 24 Stunden 365 Tage im Jahr erreichbar.</p>

  <div class="photo" style="left:610px;top:618px;width:502px;height:377px">
    <div class="abs" style="inset:0;background:linear-gradient(180deg,#d9d6d3 0%,#b8aeaa 45%,#8f8c94 75%,#a7a5ad 100%)" role="img" aria-label="Gruppenfoto des Teams am Besprechungstisch"></div>
    <div class="tab" style="width:204px;height:69px;padding-left:18px;font-size:21px;font-weight:500">Unser Team
      <span class="arrow"><svg viewBox="0 0 16 16" fill="none" stroke="#4a3a1c" stroke-width="1.4"><path d="M3 8h10M9 4l4 4-4 4"/></svg></span>
    </div>
  </div>
</section>

<section>
  <h2 class="abs section-title" style="left:88px;top:1054px">Unser Service auf einen Blick</h2>

  <div class="card" style="left:88px;top:1110px">
    <div class="fill" style="background:linear-gradient(160deg,#6c7a4d 0%,#e8e6df 40%,#b98c57 70%,#d6a775 100%)" role="img" aria-label="Holzsarg mit weißen Orchideen und Farn"></div>
    <div class="tab" style="width:184px">Erdbestattung <span class="arrow"><svg viewBox="0 0 16 16" fill="none" stroke="#4a3a1c" stroke-width="1.4"><path d="M3 8h10M9 4l4 4-4 4"/></svg></span></div>
  </div>
  <div class="card" style="left:436px;top:1110px">
    <div class="fill" style="background:linear-gradient(180deg,#6b6a67 0%,#9a9894 40%,#5c7f3f 75%,#3f6a2c 100%)" role="img" aria-label="Metallurne auf grünem Blumengesteck"></div>
    <div class="tab" style="width:198px">Feuerbestattung <span class="arrow"><svg viewBox="0 0 16 16" fill="none" stroke="#4a3a1c" stroke-width="1.4"><path d="M3 8h10M9 4l4 4-4 4"/></svg></span></div>
  </div>
  <div class="card" style="left:783px;top:1110px">
    <div class="fill" style="background:linear-gradient(180deg,#b48f86 0%,#6e6670 35%,#3d3e47 70%,#2f3038 100%)" role="img" aria-label="Laterne mit Kerze am Meer in der Abenddämmerung"></div>
    <div class="tab" style="width:184px">Seebestattung <span class="arrow"><svg viewBox="0 0 16 16" fill="none" stroke="#4a3a1c" stroke-width="1.4"><path d="M3 8h10M9 4l4 4-4 4"/></svg></span></div>
  </div>

  <div class="card text-card" style="left:88px;top:1464px">
    <svg width="40" height="54" viewBox="0 0 40 54" fill="none" stroke="#e5c48a" stroke-width="2.5"><path d="M3 2h34M3 52h34M7 2c0 14 12 18 12 25S7 40 7 52M33 2c0 14-12 18-12 25s12 13 12 25"/><path d="M10 48c4-6 16-6 20 0z" fill="#e5c48a"/></svg>
    <h3>Bestattungsvorsorge</h3>
    <p>Es ist ein paradiesmatisches Land, in dem einem gebratene Satzteile in den Mund fliegen. Nicht einmal von der allmächtigen. Es packte seine sieben Versalien.</p>
    <span class="arrow"><svg viewBox="0 0 16 16" fill="none" stroke="#4a3a1c" stroke-width="1.4"><path d="M3 8h10M9 4l4 4-4 4"/></svg></span>
  </div>
  <div class="card text-card" style="left:436px;top:1464px">
    <svg width="56" height="54" viewBox="0 0 56 54" fill="none" stroke="#e5c48a" stroke-width="2.5"><ellipse cx="28" cy="30" rx="22" ry="16"/><circle cx="40" cy="12" r="6"/><path d="M15 43v8M38 43v8M6 28H2"/></svg>
    <h3>Bestattungskosten</h3>
    <p>Es ist ein paradiesmatisches Land, in dem einem gebratene Satzteile in den Mund fliegen. Nicht einmal von der allmächtigen.</p>
    <span class="arrow"><svg viewBox="0 0 16 16" fill="none" stroke="#4a3a1c" stroke-width="1.4"><path d="M3 8h10M9 4l4 4-4 4"/></svg></span>
  </div>
  <div class="card" style="left:783px;top:1464px">
    <div class="fill" style="background:linear-gradient(160deg,#5a5450 0%,#8a8580 35%,#eef0f2 55%,#9a5e3c 75%,#7a7874 100%)" role="img" aria-label="Sarg auf Förderband beim Verladen in ein Flugzeug"></div>
    <div class="tab" style="width:184px">Überführung <span class="arrow"><svg viewBox="0 0 16 16" fill="none" stroke="#4a3a1c" stroke-width="1.4"><path d="M3 8h10M9 4l4 4-4 4"/></svg></span></div>
  </div>
</section>

<section>
  <h2 class="abs section-title" style="left:0;width:1200px;top:1852px;text-align:center">Häufig gestellte Fragen</h2>
  <div class="faq">
    <div class="faq-item"><svg viewBox="0 0 16 16" fill="none" stroke="#4a3a1c" stroke-width="1.8"><path d="M3 6l5 5 5-5"/></svg>Lorem ipsum dolor sit amet consectetur?</div>
    <div class="faq-item"><svg viewBox="0 0 16 16" fill="none" stroke="#4a3a1c" stroke-width="1.8"><path d="M3 6l5 5 5-5"/></svg>Lorem ipsum dolor sit amet consectetur adipiscing?</div>
    <div class="faq-item"><svg viewBox="0 0 16 16" fill="none" stroke="#4a3a1c" stroke-width="1.8"><path d="M3 6l5 5 5-5"/></svg>Lorem ipsum dolor sit amet?</div>
    <div class="faq-item"><svg viewBox="0 0 16 16" fill="none" stroke="#4a3a1c" stroke-width="1.8"><path d="M3 6l5 5 5-5"/></svg>Lorem ipsum dolor sit amet?</div>
    <div class="faq-item"><svg viewBox="0 0 16 16" fill="none" stroke="#4a3a1c" stroke-width="1.8"><path d="M3 6l5 5 5-5"/></svg>Lorem ipsum dolor sit amet consectetur?</div>
    <div class="faq-item"><svg viewBox="0 0 16 16" fill="none" stroke="#4a3a1c" stroke-width="1.8"><path d="M3 6l5 5 5-5"/></svg>Lorem ipsum dolor sit amet consectetur?</div>
  </div>
</section>

<section>
  <h2 class="abs section-title" style="left:0;width:1200px;top:2237px;text-align:center">Unsere Mitgliedschaften</h2>
  <div class="member" style="left:88px"><div class="badge" role="img" aria-label="Mitgliedsabzeichen"></div></div>
  <div class="member" style="left:349px"><div class="badge" role="img" aria-label="Zertifikatsabzeichen"></div></div>
  <div class="member" style="left:610px"><div class="badge" role="img" aria-label="Verbandsabzeichen"></div></div>
  <div class="member" style="left:871px"><div class="badge" role="img" aria-label="Verbandsabzeichen"></div></div>
</section>

<footer>
  <div class="footer">
    <div class="f-brand"><span class="dot"></span>Bestattungswesen Wiesentrup</div>
    <div class="f-addr"><strong>Bestattungswesen Wiesentrup</strong><br>Inhaberin Marlene Hoffmann<br>Lindenweg 14<br>09411 Wiesentrup</div>
    <div class="f-contact" style="top:278px">
      <svg viewBox="0 0 24 24" fill="none" stroke="currentColor" stroke-width="1.4"><path d="M5 3h4l2 5-2.5 1.5a11 11 0 005 5L15 12l5 2v4a2 2 0 01-2 2A16 16 0 013 5a2 2 0 012-2z"/></svg>03721 / 48 210</div>
    <div class="f-contact" style="top:308px">
      <svg viewBox="0 0 24 24" fill="none" stroke="currentColor" stroke-width="1.4"><rect x="3" y="5" width="18" height="14" rx="2"/><path d="M3 7l9 6 9-6"/></svg>info@bestattungswesen-wiesentrup.de</div>
    <div class="f-col" style="left:436px">
      <h4>Bestattungsarten</h4>
      <ul><li>Baumbestattung</li><li>Erdbestattung</li><li>Seebestattung</li><li>Feuerbestattung</li><li>Anonyme Bestattung</li><li>Besondere Bestattungen</li></ul>
    </div>
    <div class="f-col" style="left:626px">
      <h4>Im Trauerfall</h4>
      <ul><li>Erste Schritte</li><li>Leistungen</li><li>Friedhöfe</li><li>Floristik</li><li>Trauerdruck</li><li>Bestattungskosten</li></ul>
    </div>
    <div class="map" role="img" aria-label="Stadtplan mit Standort des Bestattungshauses"></div>
  </div>
  <div class="footer-bar">
    <span class="abs" style="left:89px;top:31px">Startseite</span>
    <span class="abs" style="left:173px;top:31px">Sitemap</span>
    <span class="abs" style="left:250px;top:31px">Datenschutz</span>
    <span class="abs" style="left:352px;top:31px">Impressum</span>
    <span class="abs" style="right:88px;top:31px">© Bestattungswesen Wiesentrup - All Rights Reserved</span>
  </div>
</footer>

</body>
</html>
```